Publishing company needs book cover for multi-author book

Copperleaf Lantern Publishing needs a book cover designed for a multi-author book called Quiet Orbits: Uncommon Triumph Tales from Remarkable Pathfinders. We would like to see designs that incorporates the design theme of the image attached and possibly the image itself. The book will be used by the contributing authors who are  are Healers, Psychics, Coaches, Energy Workers, Astrologers, Numerologist, Tarot Card Readers and will be using this book to both market their business and use in their practices.  The final design should communicate  these spiritual practices.
I would love to see
1. A silhouette or image of a woman holding a ball or circle with the attached art inside of.
2. The concepts in the attached art brought into a  new design or  enhancing the original art.

Target Market(s)
The clients and audiences of the contributing authors
Industry/Entity Type
Spiritual, Body Mind Spirit, Evolving Continuousness, Alternative Healing
Colors
Designer to choose colors to be used in the design.
Requirements
Must have
- Title- Quiet Orbits: Uncommon Triumph Tales from Remarkable Pathfinders. and the name of the publishing company: Copperleaf Lantern Publishing

Nice to have
- I would love to have the concept of the artwork coming to life through an image of woman, visionary, healer who is healing the world through her modalities.

Should not have
- Dimensions - 6X9

```html
<!DOCTYPE html>
<html lang="en">
<head>
<meta charset="utf-8">
<title>Quiet Orbits – Book Cover</title>
<link rel="stylesheet" href="https://fonts.googleapis.com/css2?family=Marcellus&family=Fira+Sans:wght@400&family=Source+Sans+3:wght@400&display=swap">
<style>
  :root {
    --page-bg: #ffffff;
    --band-purple: #4a3a9c;
    --band-purple-deep: #3d2f8a;
    --art-magenta: #d0319f;
    --art-pink: #e86cc6;
    --art-blue: #3d8fe0;
    --art-sky: #6fc3f0;
    --art-navy: #22257a;
    --title-white: #ffffff;
    --accent-orange: #f7a51c;
    --bullet-yellow: #ffd447;
  }
  * { margin: 0; padding: 0; box-sizing: border-box; }
  html, body {
    width: 1200px; height: 1200px; overflow: hidden;
    background: var(--page-bg);
  }
  .book-cover {
    position: absolute;
    left: 230px; top: 45px;
    width: 740px; height: 1110px;
    background: var(--band-purple);
    overflow: hidden;
  }
  .publisher-band {
    position: absolute; left: 0; top: 0;
    width: 100%; height: 75px;
    background: linear-gradient(180deg, var(--band-purple) 0%, var(--band-purple-deep) 100%);
    display: flex; align-items: center; justify-content: center;
  }
  .publisher-name {
    font-family: "Source Sans 3", sans-serif;
    font-size: 25px;
    letter-spacing: 0.34em;
    color: var(--title-white);
    padding-left: 0.34em;
  }
  .cover-art {
    position: absolute; left: 0; top: 75px;
    width: 100%; height: 880px;
    background:
      radial-gradient(circle at 62% 52%, var(--art-sky) 0%, var(--art-blue) 18%, transparent 38%),
      radial-gradient(circle at 80% 30%, var(--art-blue) 0%, transparent 35%),
      radial-gradient(ellipse at 30% 75%, var(--art-pink) 0%, transparent 45%),
      linear-gradient(180deg, var(--art-magenta) 0%, var(--art-blue) 30%, var(--art-navy) 55%, var(--art-magenta) 78%, var(--art-pink) 100%);
  }
  .title-main {
    position: absolute;
    left: 58px; top: 222px;
    font-family: "Marcellus", serif;
    font-size: 100px;
    line-height: 1;
    color: var(--title-white);
    -webkit-text-stroke: 2px var(--title-white);
    text-shadow: 2px 3px 6px rgba(30, 20, 80, 0.45);
  }
  .title-vertical {
    position: absolute;
    left: 525px; top: 120px;
    writing-mode: vertical-rl;
    font-family: "Marcellus", serif;
    font-size: 178px;
    line-height: 1;
    letter-spacing: 0.02em;
    color: rgba(255, 255, 255, 0.12);
    -webkit-text-stroke: 3px var(--title-white);
  }
  .practice-list {
    position: absolute;
    right: 224px; top: 728px;
    list-style: none;
    text-align: right;
    font-family: "Fira Sans", sans-serif;
    font-size: 23px;
    line-height: 28.6px;
    color: var(--title-white);
  }
  .practice-list li::before {
    content: "";
    display: inline-block;
    width: 6px; height: 6px;
    border-radius: 50%;
    background: var(--bullet-yellow);
    margin-right: 8px;
    vertical-align: middle;
  }
  .subtitle-band {
    position: absolute; left: 0; bottom: 0;
    width: 100%; height: 155px;
    background: linear-gradient(180deg, var(--band-purple-deep) 0%, var(--band-purple) 100%);
    display: flex; flex-direction: column; align-items: center; justify-content: center;
    gap: 8px;
    font-family: "Marcellus", serif;
    color: var(--accent-orange);
    -webkit-text-stroke: 0.8px var(--accent-orange);
  }
  .subtitle-line { font-size: 36px; line-height: 1.1; }
  .subtitle-leaders { font-size: 36px; line-height: 1.1; letter-spacing: 0.01em; }
</style>
</head>
<body>
  <main class="book-cover">
    <header class="publisher-band">
      <p class="publisher-name">Copperleaf Lantern Publishing</p>
    </header>

    <div class="cover-art" role="img" aria-label="Painted cosmic artwork in magenta, pink and blue with a large spiral swirl, moon phases and the dark silhouette of a dancing woman"></div>

    <h1 class="book-title">
      <span class="title-main">QUIET</span>
      <span class="title-vertical">ORBITS</span>
    </h1>

    <ul class="practice-list">
      <li>healers</li>
      <li>psychics</li>
      <li>coaches</li>
      <li>energy worker</li>
      <li>astrologers</li>
      <li>numerologis</li>
      <li>tarrot card readers</li>
    </ul>

    <footer class="subtitle-band">
      <p class="subtitle-line">Uncommon Triumph Tales from</p>
      <p class="subtitle-leaders">REMARKABLE&nbsp; PATHFINDERS</p>
    </footer>
  </main>
</body>
</html>
```